Create a Business Card Design Project for a new logistics company

We need a business card designed for a new company in Australia.

Type of business is logistics/trucking.

Medium will be brushed black metal card that can/will be acid etched to a brushed steel silver, acid die cut and two printed colours of our choice which will be white and pantone orange.

We have hopes that the design will be simple, modern and represent with a quick glance what our company does.

Please read instructions carefully in must have box any questions please ask.

If you are interested in this job please look at other job that we have which is very similar with logo and design

Please have a look at the things that can be done with metals cards on google images for inspiration.

Target Market(s)

Men from 20yrs of age to 60yrs of age

Industry/Entity Type

Steel

Requirements
Must have
• Must Have:
- Front of card:

Must use the company logo and name provided as attachment (see below KVR-black-background-cmyk).
Logo grey will be etched, orange and white will be printed on card. Parts of the logo could even be die cut.

The word -Freight on time, every route- on front etched, printed or die cut.

detail needed on front or back depending on your design layout.

Name
position
email
mobile

all details can be on front if a nice design is etched on the back of card or to keep front simple you can put all detail on back of card, I will leave the lay out to you.

Colours in logo are

Pantone 144 C Orange
Pantone 11-0601 White
Pantone 7539 C Gray
Pantone 426 C Black

However black will be the base of black metal card. Gray will be replaced with the etching in card revealing the silver. Orange and white will be printed on card.

have fun!!
Nice to have
• The file attached called idea is just an example of what can be designed and etched into card. Google has many more idea's for metal business cards.
Should not have
• Please don't clutter the card
No fonts smaller then 7 points

```html
<!DOCTYPE html>
<html lang="en">
<head>
<meta charset="utf-8">
<title>KVR Industries – Business Card</title>
<link rel="stylesheet" href="https://fonts.googleapis.com/css2?family=Jost:wght@400;500;600&display=swap">
<style>
  :root {
    --stage: #2a2a2a;
    --card-black: #0b0b0b;
    --orange: #f7a01c;
    --orange-deep: #f08a12;
    --white: #ffffff;
    --steel: #a9abae;
  }
  * { box-sizing: border-box; margin: 0; padding: 0; }
  html, body {
    width: 1200px; height: 798px; overflow: hidden;
    background: var(--stage);
    font-family: "Jost", "Futura", sans-serif;
  }
  .stage {
    position: relative; width: 1200px; height: 798px;
    display: flex; align-items: center; justify-content: center; gap: 60px;
  }
  .card {
    position: relative; width: 520px; height: 297px; flex: none;
    background: var(--card-black); overflow: hidden;
    box-shadow: 0 10px 30px rgba(0,0,0,.45);
  }

  /* Back: contact side */
  .back .band-orange {
    position: absolute; left: 0; right: 0; top: 62px; height: 150px;
    background: var(--orange);
  }
  .back .band-foot {
    position: absolute; left: 0; right: 0; bottom: 0; height: 16px;
    background: var(--orange);
  }
  .brand-mark { position: absolute; display: flex; align-items: center; gap: 10px; }
  .brand-dot { width: 16px; height: 16px; border-radius: 50%; background: var(--white); flex: none; }
  .brand-name { font-weight: 600; letter-spacing: 2px; line-height: 1; white-space: nowrap; }
  .back .brand-mark { left: 175px; top: 76px; }
  .back .brand-name { font-size: 20px; color: var(--card-black); }
  .back .brand-sub {
    position: absolute; left: 201px; top: 101px;
    font-size: 9px; letter-spacing: 3px; color: var(--card-black);
  }
  .back .brand-rule {
    position: absolute; left: 201px; width: 150px; top: 116px; height: 1px;
    background: var(--card-black);
  }
  .person { position: absolute; left: 201px; top: 134px; }
  .person-name { font-size: 21px; font-weight: 500; color: var(--card-black); line-height: 1.1; }
  .person-role { font-size: 13px; color: var(--white); margin-top: 4px; }
  .contacts {
    position: absolute; right: 30px; top: 222px;
    color: var(--white); font-size: 16px; line-height: 1.5;
  }
  .contact-line { display: flex; align-items: center; gap: 8px; white-space: nowrap; }
  .contact-line svg { width: 15px; height: 15px; flex: none; }

  /* Front: brand side */
  .front .brand-mark { left: 60px; top: 92px; gap: 16px; }
  .front .brand-dot { width: 34px; height: 34px; background: var(--steel); }
  .front .brand-name { font-size: 46px; color: var(--orange-deep); }
  .front .brand-sub {
    position: absolute; left: 110px; top: 144px;
    font-size: 11px; letter-spacing: 4px; color: var(--white);
  }
  .front .brand-rule {
    position: absolute; left: 110px; right: 40px; top: 164px; height: 2px;
    background: var(--steel);
  }
  .front .tagline {
    position: absolute; left: 110px; top: 176px;
    font-size: 21px; letter-spacing: 1px; color: var(--white); white-space: nowrap;
  }
</style>
</head>
<body>
<main class="stage">
  <section class="card back" aria-label="Card back with contact details">
    <div class="band-orange"></div>
    <div class="band-foot"></div>
    <div class="brand-mark">
      <span class="brand-dot"></span>
      <span class="brand-name">KVR</span>
    </div>
    <p class="brand-sub">INDUSTRIES Pty Ltd</p>
    <div class="brand-rule"></div>
    <div class="person">
      <p class="person-name">Your Name</p>
      <p class="person-role">Designation</p>
    </div>
    <div class="contacts">
      <p class="contact-line">
        <svg viewBox="0 0 16 16"><circle cx="8" cy="8" r="7" fill="none" stroke="#fff" stroke-width="1.4"/><path d="M5.5 4.5l1.5 1.5-1 1a5 5 0 0 0 3 3l1-1 1.5 1.5-1 1.2C7.5 12.5 3.5 8.5 4.3 5.5z" fill="#fff"/></svg>
        000 111 2222
      </p>
      <p class="contact-line">
        <svg viewBox="0 0 16 16"><rect x="1" y="3.5" width="14" height="9" fill="#fff"/><path d="M1 3.5l7 5 7-5" fill="none" stroke="#0b0b0b" stroke-width="1.2"/></svg>
        info@kvrfreight.com
      </p>
    </div>
  </section>

  <section class="card front" aria-label="Card front with company name and tagline">
    <div class="brand-mark">
      <span class="brand-dot"></span>
      <span class="brand-name">KVR</span>
    </div>
    <p class="brand-sub">INDUSTRIES Pty Ltd</p>
    <div class="brand-rule"></div>
    <p class="tagline">FREIGHT ON TIME, EVERY ROUTE</p>
  </section>
</main>
</body>
</html>
```